Crust Harbor Hotel Coupon

Would like to design a coupon that is for hotels' staff and to be dropped off at the hotel front office anytime someone calls from a hotel and as a Thank You for hotel staff for recommending us. Coupon value to be $ 2.00. Should say Thank You or Thank you for recommending us. Need our phone number 250 614 3785 on it. Color scheme to be Green and Red as in the attached logo. Coupon to be designed for printing size 3.5 inches high and 7.5 inches wide. Rear should say Fastest Delivery, Favourite Pizza for Sports teams etc. Ask for group deals. Attached logo to be on the coupon. Coupon should say coupon # and space left for us write number

```html
<!DOCTYPE html>
<html lang="en">
<head>
<meta charset="utf-8">
<title>Crust Harbor Hotel Coupon</title>
<link rel="stylesheet" href="https://fonts.googleapis.com/css2?family=Montserrat:ital,wght@0,300;0,400;0,600;0,700;0,800;1,700&display=swap">
<style>
  :root {
    --red: #c9302f;
    --red-deep: #b52a2a;
    --orange: #f07a2b;
    --yellow: #ffe12a;
    --gold: #f8b62a;
    --white: #ffffff;
    --backdrop: #e4e4e4;
    --photo-warm: #d98a55;
    --photo-dark: #5b4a44;
    --social-blue: #4d5b9e;
    --social-violet: #8a3fa8;
  }
  * { margin: 0; padding: 0; box-sizing: border-box; }
  html, body { width: 1200px; height: 1200px; overflow: hidden; }
  body {
    background: var(--backdrop);
    font-family: "Montserrat", sans-serif;
    color: var(--white);
    position: relative;
  }
  .coupon-frame {
    position: absolute;
    left: 50px;
    top: 344px;
    width: 1100px;
    height: 512px;
    overflow: hidden;
  }
  .coupon {
    position: absolute;
    left: 0;
    top: 0;
    width: 1209px;
    height: 563px;
    transform: scale(0.9098);
    transform-origin: 0 0;
    background: linear-gradient(115deg, var(--red) 0%, var(--red-deep) 55%, var(--red) 100%);
  }
  .coupon-art { position: absolute; inset: 0; }
  .brand {
    position: absolute;
    left: 34px;
    top: 70px;
    display: flex;
    align-items: center;
    gap: 14px;
    font-weight: 800;
    font-size: 44px;
    letter-spacing: 0.5px;
  }
  .brand-dot {
    width: 34px; height: 34px;
    border-radius: 50%;
    background: var(--white);
    flex: none;
  }
  .perk {
    position: absolute;
    left: 20px;
    width: 260px;
    padding: 8px 0 8px 38px;
    border-radius: 22px 0 0 22px;
    background: linear-gradient(90deg, var(--orange) 60%, rgba(240,122,43,0) 100%);
    font-style: italic;
    font-weight: 700;
    font-size: 20px;
    line-height: 24px;
  }
  .perk-delivery { top: 224px; }
  .perk-teams { top: 284px; }
  .group-deals {
    position: absolute;
    left: 58px;
    top: 398px;
    font-style: italic;
    font-weight: 700;
    font-size: 29px;
    line-height: 35px;
  }
  .coupon-number {
    position: absolute;
    left: 748px;
    top: 28px;
    font-weight: 700;
    font-size: 36px;
  }
  .number-line {
    position: absolute;
    left: 965px;
    top: 73px;
    width: 220px;
    border-top: 2px dashed var(--gold);
  }
  .value-label {
    position: absolute;
    right: 71px;
    top: 108px;
    font-weight: 400;
    font-size: 32px;
  }
  .value-amount {
    position: absolute;
    right: 64px;
    top: 134px;
    font-weight: 700;
    font-size: 96px;
    line-height: 110px;
  }
  .thanks-band {
    position: absolute;
    left: 700px;
    top: 250px;
    width: 490px;
    height: 158px;
    border-radius: 80px;
    background: linear-gradient(90deg, rgba(240,122,43,0) 0%, rgba(240,122,43,0.85) 50%, var(--orange) 100%);
  }
  .thanks-title {
    position: absolute;
    left: 680px;
    top: 250px;
    font-weight: 700;
    font-size: 82px;
    line-height: 100px;
  }
  .thanks-sub {
    position: absolute;
    left: 680px;
    top: 344px;
    color: var(--yellow);
    font-weight: 400;
    font-size: 44px;
  }
  .order-label {
    position: absolute;
    left: 654px;
    top: 446px;
    color: var(--yellow);
    font-style: italic;
    font-weight: 700;
    font-size: 23px;
  }
  .order-phone {
    position: absolute;
    left: 654px;
    top: 474px;
    font-weight: 700;
    font-size: 34px;
  }
  .social {
    position: absolute;
    top: 461px;
    width: 50px; height: 50px;
    border-radius: 50%;
  }
  .social-one { left: 947px; background: var(--social-blue); }
  .social-two { left: 1018px; background: var(--social-violet); }
  .social-map { left: 1090px; background: var(--yellow); }
  .social-map svg { width: 50px; height: 50px; }
</style>
</head>
<body>
  <div class="coupon-frame">
    <div class="coupon">
      <svg class="coupon-art" viewBox="0 0 1209 563" width="1209" height="563">
        <defs>
          <linearGradient id="photoTone" x1="0" y1="0" x2="1" y2="1">
            <stop offset="0" stop-color="var(--photo-dark)"/>
            <stop offset="0.35" stop-color="var(--photo-warm)"/>
            <stop offset="0.8" stop-color="#e9b07c"/>
            <stop offset="1" stop-color="var(--photo-dark)"/>
          </linearGradient>
          <linearGradient id="stripeTone" x1="0" y1="0" x2="0" y2="1">
            <stop offset="0" stop-color="var(--yellow)"/>
            <stop offset="1" stop-color="var(--orange)"/>
          </linearGradient>
        </defs>
        <polygon points="373,0 648,0 488,563 183,563" fill="url(#photoTone)" role="img" aria-label="Photo of a sliced pizza topped with chicken, peppers and cheese"/>
        <polygon points="648,0 683,0 523,563 488,563" fill="url(#stripeTone)"/>
        <polygon points="683,0 718,0 558,563 523,563" fill="var(--white)"/>
        <polygon points="718,0 728,0 568,563 558,563" fill="var(--gold)"/>
      </svg>

      <div class="brand"><span class="brand-dot"></span>Crust Harbor</div>

      <div class="perk perk-delivery">Fastest Delivery</div>
      <div class="perk perk-teams">Favourite Pizza<br>for Sports teams</div>
      <div class="group-deals">Ask for<br>group<br>deals</div>

      <div class="coupon-number">coupon #</div>
      <div class="number-line"></div>

      <div class="value-label">Coupon value to be</div>
      <div class="value-amount">$ 2.00</div>

      <div class="thanks-band"></div>
      <div class="thanks-title">Thank you</div>
      <div class="thanks-sub">for recommending us</div>

      <div class="order-label">Order Now</div>
      <div class="order-phone">250 614 3785</div>

      <div class="social social-one"></div>
      <div class="social social-two"></div>
      <div class="social social-map">
        <svg viewBox="0 0 50 50" role="img" aria-label="Location">
          <path d="M25 12a9 9 0 0 0-9 9c0 7 9 17 9 17s9-10 9-17a9 9 0 0 0-9-9z" fill="var(--red)"/>
          <circle cx="25" cy="21" r="3.5" fill="var(--yellow)"/>
        </svg>
      </div>
    </div>
  </div>
</body>
</html>
```